Brivanta.com the Free Online Tutorial Needs a New Web Design

We need a new web design for our existing website, Brivanta.com. We provide a Free Online Tutorial of any code, like HTML, CSS, PHP, Jquery, javascript etc, including online editor.
We would like to see designs that interesting, simple, interactive, and be a very comfortable place to read in a long time.
We need 2 pages design for:
1. Home Page (http://brivanta.com) and
2. Listing Page (http://brivanta.com/tutorial/833/sql/sql-basics/sql-and-or-operator.html)
For Listing Page We need nice "Left Menu" at left side and Content Page (min 728px) at right side.
I need File PSD and/or Vector Only, without HTML code.
Online
2 page

```html
<!DOCTYPE html>
<html lang="en">
<head>
<meta charset="utf-8">
<title>Brivanta – A Place for Learning and Trying of any Code</title>
<link href="https://fonts.googleapis.com/css2?family=Oswald:wght@300;400;500&family=Lato:wght@400;700&display=swap" rel="stylesheet">
<style>
:root{
  --black:#050505;
  --ink:#2a2a2a;
  --red:#f2514e;
  --blue:#1576c8;
  --green:#67ae3e;
  --yellow:#fab01c;
  --label:#e9e9e9;
  --footer:#2b2b2b;
  --tile-top:#333;
  --tile-bottom:#1d1d1d;
  --head:"Oswald",sans-serif;
  --body:"Lato",sans-serif;
}
*{box-sizing:border-box;margin:0;padding:0}
html,body{width:759px;height:1200px;overflow:hidden;background:#fff}
body{position:relative;font-family:var(--body);color:var(--ink)}
a{text-decoration:none}
.abs{position:absolute}
.panel-dark{background:linear-gradient(180deg,var(--tile-top),var(--tile-bottom))}

/* header */
.site-header{left:0;top:0;width:759px;height:60px;background:var(--black)}
.brand{left:83px;top:14px;display:flex;align-items:center;gap:8px}
.brand-mark{width:26px;height:26px}
.brand-name{font-family:var(--head);font-weight:400;font-size:25px;color:#fff;line-height:1}
.tagline{left:212px;top:29px;font-family:var(--head);font-weight:400;font-size:10.5px;color:#fff}
.btn-small{top:8px;height:16px;border-radius:2px;font-size:8.5px;color:#111;display:flex;align-items:center;justify-content:center;font-family:var(--body)}
.btn-login{left:570px;width:50px;background:var(--yellow)}
.btn-register{left:626px;width:50px;background:var(--green);color:#fff}
.search{top:31px;left:519px;width:157px;height:19px;display:flex}
.search-field{flex:1;background:#fff;font-size:7px;color:#333;display:flex;align-items:center;padding-left:6px}
.search-btn{width:19px;height:19px;background:#111;display:flex;align-items:center;justify-content:center}

/* nav */
.main-nav{left:0;top:60px;width:759px;height:29px;background:var(--red)}
.main-nav ul{list-style:none;position:absolute;left:83px;top:0;display:flex;height:29px}
.main-nav li{font-family:var(--head);font-weight:400;font-size:10.5px;color:#fff;padding:0 13px;display:flex;align-items:center;border-right:1px solid rgba(255,255,255,.35)}
.main-nav li.active{background:var(--blue)}
.main-nav li:last-child{border-right:0}
.try-it{left:634px;top:0;width:42px;height:29px;background:var(--green);color:#fff;font-family:var(--head);font-size:10.5px;display:flex;align-items:center;justify-content:center}

/* hero */
.hero{left:0;top:89px;width:759px;height:208px;background:radial-gradient(ellipse at 30% 40%,#fafafa 0,#e4e4e4 70%)}
.hero-art{left:83px;top:16px;width:220px;height:178px;border-radius:6px;background:linear-gradient(180deg,#1b1b1b 0 72%,#c9c9c9 72% 80%,#b0b0b0 80% 90%,#dcdcdc 90%)}
.hero-art::after{content:"";position:absolute;left:9px;top:9px;width:202px;height:110px;background:radial-gradient(circle at 40% 50%,#fff 0,#eef0f4 60%,#d7dbe2 100%)}
.hero-title{left:340px;top:47px;width:332px;text-align:center;font-family:var(--head);font-weight:400;font-size:19px;line-height:26px;color:#2d2d2d}
.cta{left:442px;top:105px;width:130px;height:33px;background:#111;display:flex;align-items:center;justify-content:center;font-family:var(--head);font-weight:400;color:#fff;font-size:16px}
.dots{left:346px;top:182px;display:flex;gap:6px}
.dots span{width:12px;height:12px;border-radius:50%;background:#888}
.dots span.on{background:var(--red);border:2px solid #555}

/* section titles */
.section-title{left:0;width:759px;font-family:var(--head);font-weight:300;font-size:23px;color:#222;display:flex;justify-content:center;align-items:center;gap:10px}
.section-title::before,.section-title::after{content:"";width:60px;height:7px;background:repeating-linear-gradient(180deg,#aaa 0 1px,transparent 1px 3px)}
.section-sub{left:0;width:759px;text-align:center;font-size:10px;color:#555}

/* tutorial tiles */
.tile{width:141px;height:128px}
.tile-art{position:absolute;left:0;top:0;width:141px;height:101px}
.tile-icon{position:absolute;left:50px;top:16px;width:40px;height:40px;background:#fff;border-radius:4px}
.tile-icon.round{border-radius:50%;width:44px;left:48px}
.tile-caption{position:absolute;left:0;top:79px;width:141px;text-align:center;font-family:var(--head);font-weight:400;color:#fff;font-size:11px}
.tile-caption small{font-size:9px;margin-left:4px}
.tile-label{position:absolute;left:0;top:101px;width:141px;height:27px;background:var(--label);display:flex;align-items:center;justify-content:center;font-family:var(--head);font-weight:300;font-size:11px;color:#222}

/* about band */
.about{left:0;top:676px;width:759px;height:111px;background:var(--black)}
.about::before{content:"";position:absolute;left:0;top:0;width:759px;height:3px;background:linear-gradient(90deg,var(--blue) 0 50%,var(--green) 50%)}
.about::after{content:"";position:absolute;left:0;bottom:0;width:759px;height:3px;background:linear-gradient(90deg,var(--red) 0 50%,var(--yellow) 50%)}
.about .section-title{color:#fff;font-size:15px;font-weight:400;top:22px}
.about .section-title::before,.about .section-title::after{background:repeating-linear-gradient(180deg,#777 0 1px,transparent 1px 3px)}
.about p{position:absolute;left:90px;top:50px;width:579px;text-align:center;color:#fff;font-size:10px;line-height:13.5px}

/* featured cards */
.card{width:143px;height:82px}
.card-art{position:absolute;left:0;top:0;width:143px;height:58px;background:var(--black);overflow:hidden}
.card-art .side{position:absolute;left:0;top:0;width:64px;height:58px}
.card-art .corner{position:absolute;right:0;top:0;width:0;height:0;border-top:22px solid;border-left:22px solid transparent}
.card-text{position:absolute;left:69px;top:11px;color:#fff;font-family:var(--head);font-weight:400;font-size:9px;line-height:12.5px}
.card-text small{font-size:7px}
.card-label{position:absolute;left:0;top:58px;width:143px;height:24px;background:var(--label);display:flex;align-items:center;justify-content:center;font-family:var(--head);font-weight:300;font-size:10.5px;color:#222}

/* footer */
.site-footer{left:0;top:967px;width:759px;height:191px;background:var(--footer)}
.footer-col{top:0;height:191px}
.footer-col h3{height:23px;font-family:var(--head);font-weight:400;font-size:10.5px;color:#fff;display:flex;align-items:center;justify-content:center}
.footer-col ul{list-style:none;padding:9px 0 0 0}
.footer-col li{font-size:7.5px;color:#ddd;height:15.4px;white-space:nowrap;overflow:hidden}
.footer-col li::before{content:"›";margin-right:6px;color:#aaa}
.bottom-bar{left:0;top:1158px;width:759px;height:42px;background:var(--black)}
.bottom-links{left:83px;top:7px;font-size:8px;color:#fff;line-height:15px;font-weight:700}
.bottom-links span{margin-right:5px}
.bottom-links .current{color:var(--red)}
.bottom-search{left:314px;top:12px;width:157px;height:19px;display:flex}
.find-us{left:543px;top:7px;font-size:8px;color:#fff;font-weight:700;display:flex;align-items:center;gap:5px}
.social{width:14px;height:14px;background:#3d5a8a;border-radius:2px}
.store{width:46px;height:14px;background:#222;border:1px solid #555;border-radius:2px}
.copyright{left:550px;top:27px;font-size:7.5px;color:#fff}
</style>
</head>
<body>

<header class="abs site-header">
  <div class="abs brand">
    <svg class="brand-mark" viewBox="0 0 26 26" aria-hidden="true"><rect width="26" height="26" fill="#fff"/></svg>
    <span class="brand-name">Brivanta</span>
  </div>
  <div class="abs tagline">A Place for Learning and Trying of any Code</div>
  <a class="abs btn-small btn-login">Login</a>
  <a class="abs btn-small btn-register">Register</a>
  <div class="abs search">
    <div class="search-field">Search by Findly Engine..</div>
    <div class="search-btn"><svg width="11" height="11" viewBox="0 0 11 11"><circle cx="4.5" cy="4.5" r="3.3" fill="none" stroke="#fff" stroke-width="1.4"/><line x1="7" y1="7" x2="10.3" y2="10.3" stroke="#fff" stroke-width="1.6"/></svg></div>
  </div>
</header>

<nav class="abs main-nav">
  <ul>
    <li class="active">HOME</li><li>HTML</li><li>CSS</li><li>JAVASCRIPT</li><li>PHP</li><li>SQL</li><li>JQUERY</li><li>JSON</li><li>MORE..</li>
  </ul>
  <div class="abs try-it">TRY IT</div>
</nav>

<section class="abs hero">
  <div class="abs hero-art" role="img" aria-label="Desktop monitor showing web technology icons"></div>
  <h1 class="abs hero-title">Lorem ipsum dolor sit amet consectetuer adipiscing elit sed diam nonummy nibh</h1>
  <a class="abs cta">GET STARTED</a>
  <div class="abs dots"><span></span><span class="on"></span><span></span><span></span></div>
</section>

<h2 class="abs section-title" style="top:314px">Tutorials Library</h2>
<p class="abs section-sub" style="top:344px">Free Online Tutorials &amp; Courses</p>

<div class="abs tile" style="left:83px;top:376px"><div class="tile-art panel-dark"><div class="tile-icon"></div><div class="tile-caption">HTML5<small>Brivanta</small></div></div><div class="tile-label">HTML5 Tutorial</div></div>
<div class="abs tile" style="left:234px;top:376px"><div class="tile-art panel-dark"><div class="tile-icon"></div><div class="tile-caption">CSS3<small>Brivanta</small></div></div><div class="tile-label">CSS3 Tutorial</div></div>
<div class="abs tile" style="left:384px;top:376px"><div class="tile-art panel-dark"><div class="tile-icon"></div><div class="tile-caption">Javascript<small>Brivanta</small></div></div><div class="tile-label">Javascript Tutorial</div></div>
<div class="abs tile" style="left:535px;top:376px"><div class="tile-art panel-dark"><div class="tile-icon round"></div><div class="tile-caption">PHP<small>Brivanta</small></div></div><div class="tile-label">PHP Tutorial</div></div>

<div class="abs tile" style="left:83px;top:524px"><div class="tile-art panel-dark"><svg style="position:absolute;left:52px;top:14px" width="36" height="44" viewBox="0 0 36 44"><g fill="#fff"><ellipse cx="18" cy="6" rx="18" ry="6"/><path d="M0 10c0 3.3 8 6 18 6s18-2.7 18-6v8c0 3.3-8 6-18 6S0 21.3 0 18z"/><path d="M0 22c0 3.3 8 6 18 6s18-2.7 18-6v8c0 3.3-8 6-18 6S0 33.3 0 30z"/><path d="M0 34c0 3.3 8 6 18 6s18-2.7 18-6v4c0 3.3-8 6-18 6S0 41.3 0 38z"/></g></svg><div class="tile-caption">SQL<small>Brivanta</small></div></div><div class="tile-label">SQL Tutorial</div></div>
<div class="abs tile" style="left:234px;top:524px"><div class="tile-art panel-dark"><div class="tile-icon round"></div><div class="tile-caption">JQUERY<small>Brivanta</small></div></div><div class="tile-label">JQUERY Tutorial</div></div>
<div class="abs tile" style="left:384px;top:524px"><div class="tile-art panel-dark"><div class="tile-icon"></div><div class="tile-caption">MYSQL<small>Brivanta</small></div></div><div class="tile-label">MYSQL Tutorial</div></div>
<div class="abs tile" style="left:535px;top:524px"><div class="tile-art panel-dark"><div class="tile-icon round"></div><div class="tile-caption">JSON<small>Brivanta</small></div></div><div class="tile-label">JSON Tutorial</div></div>

<section class="abs about">
  <h2 class="abs section-title">The Free Online Tutorials Place</h2>
  <p>Brivanta is a place for Learning, testing, and examples for web building. The Examples in each chapter might be simplified to improve your basic understanding. With Brivanta You will feel much easier than ever to learn about HTML including online code editor for each chapter, so you can edit, modify and execute the code.</p>
</section>

<h2 class="abs section-title" style="top:804px">Featured Tryit Yourself</h2>

<div class="abs card" style="left:83px;top:860px"><div class="card-art"><div class="side panel-dark"></div><div class="corner" style="border-top-color:var(--blue)"></div><div class="card-text">HTML 5<br>Try it Yourself<br><small>Brivanta</small></div></div><div class="card-label">HTML5 Examples</div></div>
<div class="abs card" style="left:233px;top:860px"><div class="card-art"><div class="side panel-dark"></div><div class="corner" style="border-top-color:var(--green)"></div><div class="card-text">HTML 5 CANVAS<br>Try it Yourself<br><small>Brivanta</small></div></div><div class="card-label">Canvas Examples</div></div>
<div class="abs card" style="left:383px;top:860px"><div class="card-art"><div class="side panel-dark"></div><div class="corner" style="border-top-color:var(--red)"></div><div class="card-text">SQL<br>Try it Yourself<br><small>Brivanta</small></div></div><div class="card-label">SQL Examples</div></div>
<div class="abs card" style="left:533px;top:860px"><div class="card-art"><div class="side panel-dark"></div><div class="corner" style="border-top-color:var(--yellow)"></div><div class="card-text">Online Code<br>Try it Yourself<br><small>Brivanta</small></div></div><div class="card-label">Online Code Editor</div></div>

<footer class="abs site-footer">
  <div class="abs footer-col" style="left:83px;width:116px"><h3 style="background:var(--blue)">Random HTML5</h3><ul><li>Time Tag In Html5</li><li>P In Html5</li><li>Col Tag In Html</li><li>Progress In Html5</li><li>Text Formating Overview I..</li><li>I Tag In Html5</li><li>Command</li><li>Rp In Html5</li><li>Q Tag In Html5</li><li>Footer In Html5</li></ul></div>
  <div class="abs footer-col" style="left:199px;width:109px"><h3 style="background:var(--green)">Random Canvas</h3><ul><li>Canvas Custom Paths</li><li>Canvas Line Join</li><li>Canvas Image Crop</li><li>Canvas Fill Style</li><li>Canvas Quadratic Curve</li><li>Canvas Introduction</li><li>Canvas Semicircles</li><li>Canvas Text Basics</li><li>Canvas Line Cap</li><li>Canvas Pattern</li></ul></div>
  <div class="abs footer-col" style="left:316px;width:116px"><h3 style="background:var(--red);margin-left:-8px">Random Javascript</h3><ul><li>Javascript Browser Window</li><li>JS Global unescape()</li><li>JS Global Function eval()</li><li>Javascript Operators</li><li>JS RegExp ignoreCase</li><li>Javascript Variables</li><li>JS DOM Body Object</li><li>JS DOM Frameset Object</li><li>Javascript Comparison - L..</li><li>Javascript Browser Compat..</li></ul></div>
  <div class="abs footer-col" style="left:440px;width:108px"><h3 style="background:var(--yellow);margin-left:-8px">Random Try it</h3><ul><li>HTML Symbols Examples</li><li>Colors RGB in HTML</li><li>progress tag without valu..</li><li>title tag example</li><li>iframe tag Example</li><li>colgroup tag example</li><li>ins tag example</li><li>External Style Sheet CSS ..</li><li>hr tag example</li><li>h2 tag example</li></ul></div>
  <div class="abs footer-col" style="left:556px;width:120px"><h3 style="background:var(--black);margin-left:-8px">Random Articles</h3><ul><li>How to Auto Select All Te..</li><li>How to Make Sitemap.xml</li><li>How to Make Drop Down Men..</li><li>How to make WHOIS lookups..</li><li>How to get an input text ..</li><li>Changing text with innerh..</li><li>Make A lot of Circle Anim..</li><li>How to Make SQL Syntax Hi..</li><li>Create Transparency Anima..</li><li>How to Make Drop Down Men..</li></ul></div>
</footer>

<div class="abs bottom-bar">
  <div class="abs bottom-links">
    <span class="current">Tutorial</span><span>Articles</span><span>Try it</span><span>Canvas</span><span>Webtools</span><br>
    <span>About</span><span>Terms</span><span>Privacy</span><span>Disclaimer</span><span>Contact</span><span>FAQ</span>
  </div>
  <div class="abs bottom-search">
    <div class="search-field">Search by Brivanta..</div>
    <div class="search-btn"><svg width="11" height="11" viewBox="0 0 11 11"><circle cx="4.5" cy="4.5" r="3.3" fill="none" stroke="#fff" stroke-width="1.4"/><line x1="7" y1="7" x2="10.3" y2="10.3" stroke="#fff" stroke-width="1.6"/></svg></div>
  </div>
  <div class="abs find-us">Find Us on <span class="social"></span><span class="social" style="background:#4a8a6a"></span><span class="store" aria-label="Findly Play"></span></div>
  <div class="abs copyright">© 2015 Brivanta. All Rights Reserved.</div>
</div>

</body>
</html>
```